Talvick Industrial Maintenance Business Card

Design a business card with the following information, logo must be included.
Talvick Industrial Maintenance
Dan Pelfrey Jr.
Pone 555-214-7608
email dan.pelfrey.jr@mailvantor.com

```html
<!DOCTYPE html>
<html lang="en">
<head>
<meta charset="utf-8">
<title>Talvick Industrial Maintenance Business Card</title>
<link rel="stylesheet" href="https://fonts.googleapis.com/css2?family=Montserrat:wght@400;500;700&display=swap">
<style>
  :root {
    --backdrop: #8c8c8c;
    --card: #ffffff;
    --brand-blue: #1a6fb8;
    --ink: #1e1e1e;
    --muted: #8a8a8a;
  }
  * { margin: 0; padding: 0; box-sizing: border-box; }
  html, body { width: 1200px; height: 1017px; overflow: hidden; }
  body {
    background: var(--backdrop);
    font-family: "Montserrat", sans-serif;
    position: relative;
  }
  .card {
    position: absolute;
    width: 540px;
    height: 310px;
    background: var(--card);
    box-shadow: 0 6px 18px rgba(0,0,0,0.18);
  }
  .card--front { left: 80px; top: 110px; }
  .card--back { left: 580px; top: 580px; }

  .brand {
    position: absolute;
    display: flex;
    align-items: center;
    gap: 14px;
    color: var(--brand-blue);
    font-weight: 700;
  }
  .brand__mark {
    width: 56px; height: 56px;
    border-radius: 50%;
    border: 6px solid var(--brand-blue);
    flex: none;
  }
  .brand__name {
    font-size: 22px;
    line-height: 1.15;
    letter-spacing: 0.04em;
    text-transform: uppercase;
  }
  .card--front .brand { left: 50%; top: 50%; transform: translate(-50%, -50%); }
  .card--back .brand { left: 150px; top: 46px; }
  .card--back .brand__mark { width: 46px; height: 46px; border-width: 5px; }
  .card--back .brand__name { font-size: 18px; }

  .divider {
    position: absolute;
    left: 36px; right: 36px; top: 168px;
    height: 1.5px;
    background: var(--brand-blue);
  }
  .holder {
    position: absolute;
    left: 40px; top: 214px;
    font-size: 30px;
    font-weight: 700;
    color: var(--brand-blue);
  }
  .contact {
    position: absolute;
    right: 36px; top: 112px;
    list-style: none;
    font-size: 13px;
    color: var(--ink);
  }
  .contact li { display: flex; align-items: center; gap: 8px; margin-bottom: 6px; }
  .contact svg { width: 13px; height: 13px; fill: var(--muted); flex: none; }
</style>
</head>
<body>
  <section class="card card--front">
    <div class="brand">
      <span class="brand__mark"></span>
      <span class="brand__name">Talvick<br>Industrial Maintenance</span>
    </div>
  </section>

  <section class="card card--back">
    <div class="brand">
      <span class="brand__mark"></span>
      <span class="brand__name">Talvick<br>Industrial Maintenance</span>
    </div>
    <ul class="contact">
      <li>
        <svg viewBox="0 0 24 24" aria-hidden="true"><path d="M6.6 10.8c1.4 2.8 3.8 5.1 6.6 6.6l2.2-2.2c.3-.3.7-.4 1-.2 1.1.4 2.3.6 3.6.6.6 0 1 .4 1 1V20c0 .6-.4 1-1 1C10.6 21 3 13.4 3 4c0-.6.4-1 1-1h3.5c.6 0 1 .4 1 1 0 1.3.2 2.5.6 3.6.1.3 0 .7-.2 1z"/></svg>
        <span>555-214-7608</span>
      </li>
      <li>
        <svg viewBox="0 0 24 24" aria-hidden="true"><path d="M2 5h20v14H2zm2 2v.5l8 5 8-5V7zm0 2.8V17h16V9.8l-8 5z"/></svg>
        <span>dan.pelfrey.jr@mailvantor.com</span>
      </li>
    </ul>
    <div class="divider"></div>
    <p class="holder">Dan Pelfrey Jr.</p>
  </section>
</body>
</html>
```